Website for Private Psychologist

DO NOT CONTACT ME PRIVATELY

I am a Psychologist offering psychotherapy for individuals and couples, and clinical consultation and training and education for mental and medical health professionals and agencies.

I need a redesign of my website

5 Pages (content is attached for each page)
Home
Jungian Psychotherapy
Clinical Consultation & Professional Development
Curriculum Vitae & Publications
Practice Policies and Forms

Designs can be based on these style websites
https://lqmindcare.info; https://pdtarn.org/; https://dorabellcroftcounselling.com/

Design Concepts
Minimalist Layout: Clean and uncluttered layout with generous white space, allowing the content and visuals to stand out'

Keep a linear, uncluttered, professional design.

Please use only royalty free images and google fonts. Please provide links to any stock images used to verify license.

Target Market(s)

private individual or couples seeking psychotherapy

Industry/Entity Type

Psychotherapy

Number of Pages Required

5+ page

Requirements
Should not have
• No search feature

```html
<!DOCTYPE html>
<html lang="en">
<head>
<meta charset="utf-8">
<title>Dorian Pellquist — Doctor of Psychology</title>
<link rel="stylesheet" href="https://fonts.googleapis.com/css2?family=Roboto+Slab:wght@300;400;500&family=Roboto:wght@300;400;500&display=swap">
<style>
:root{
  --ink:#111111;
  --text:#3a3a3a;
  --muted:#777777;
  --line:#cfcfcf;
  --paper:#ffffff;
  --mist:#f2f2f2;
  --night:#232323;
  --slate:#4a4a4a;
  --chip:#e4e4e4;
  --light:#f4f4f4;
}
*{margin:0;padding:0;box-sizing:border-box}
html,body{width:1200px;height:3000px;overflow:hidden;background:var(--paper)}
body{font-family:"Roboto",Arial,sans-serif;color:var(--text);position:relative}
section,footer{position:absolute;left:0;width:1200px}
.abs{position:absolute}

/* brand */
.brand{position:absolute;border-left:2px solid var(--ink);padding-left:12px}
.brand-name{font-family:"Roboto Slab",Georgia,serif;font-size:20px;font-weight:500;color:var(--ink);line-height:1.2;white-space:nowrap}
.brand-sub{font-family:"Roboto Slab",Georgia,serif;font-size:9px;color:var(--muted);letter-spacing:.3px;text-transform:uppercase;white-space:nowrap}

/* labels */
.eyebrow{font-family:"Roboto Slab",Georgia,serif;font-size:14px;letter-spacing:4px;color:var(--text);text-transform:uppercase;white-space:nowrap}
.rule{position:absolute;height:1px;background:var(--line)}
.heading{font-family:"Roboto Slab",Georgia,serif;font-weight:400;color:var(--ink);font-size:23px;line-height:1.42;white-space:nowrap}
.copy{font-size:12.5px;line-height:21.5px;color:var(--text)}

/* hero */
.hero{top:0;height:520px;background:linear-gradient(180deg,#f3f3f3 0%,#ffffff 45%,#ffffff 75%,#d9d9d9 100%);overflow:hidden}
.hero-art{position:absolute;left:640px;top:0;width:560px;height:520px;background:radial-gradient(ellipse at 70% 40%,#3a3a3a 0%,#1c1c1c 55%,#2c2c2c 100%)}
.hero-call{position:absolute;left:790px;top:37px;font-size:12px;color:var(--light);display:flex;align-items:center;gap:8px;white-space:nowrap}
.hero-call b{font-weight:500}
.menu{position:absolute;left:1056px;top:34px}
.hero-title{position:absolute;left:100px;top:183px;width:500px;font-size:31px;line-height:1.3;font-family:"Roboto Slab",Georgia,serif;color:var(--ink);font-weight:400;white-space:nowrap}
.hero-lead{position:absolute;left:100px;top:330px;width:360px;font-size:12.5px;line-height:21px;color:var(--ink)}
.btn{position:absolute;left:100px;top:400px;width:243px;height:47px;background:var(--ink);color:#fff;font-family:"Roboto Slab",Georgia,serif;font-size:17px;display:flex;align-items:center;justify-content:center}

/* about */
.about{top:520px;height:590px;background:var(--paper)}
.portrait{position:absolute;left:236px;top:95px;width:312px;height:414px;background:linear-gradient(160deg,#8a7e74 0%,#4b4540 50%,#1e1c1b 100%)}
.call-block{position:absolute;left:616px;top:462px;border-left:2px solid var(--ink);padding-left:13px}
.call-block .lbl{font-size:11px;color:var(--ink);display:flex;align-items:center;gap:6px}
.call-block .num{font-family:"Roboto Slab",Georgia,serif;font-size:17px;font-weight:500;color:var(--ink);margin-top:4px}

/* services */
.services{top:1110px;height:620px;background:var(--mist)}
.svc-art{position:absolute;left:700px;top:0;width:192px;height:224px;background:radial-gradient(circle at 45% 45%,#8c2f3c 0%,#6a6f7a 30%,#b6bfc8 70%,#d9dee3 100%);border-radius:0 0 96px 96px}
.badge{position:absolute;left:860px;top:72px;width:106px;height:106px;border-radius:50%;background:var(--slate);color:#fff;display:flex;align-items:center;justify-content:center;text-align:center;font-family:"Roboto Slab",Georgia,serif;font-size:14px;letter-spacing:2.5px;line-height:1.5;font-weight:500}
.card{position:absolute;top:277px;width:227px;height:255px;background:var(--paper);padding:26px 28px}
.card h3{font-family:"Roboto Slab",Georgia,serif;font-weight:400;font-size:12.5px;letter-spacing:1.5px;color:var(--ink);margin-top:12px;white-space:nowrap}
.card p{font-size:12.5px;line-height:21.5px;color:var(--text);margin-top:16px}
.card .go{position:absolute;left:28px;bottom:22px}

/* experience */
.experience{top:1730px;height:540px}
.exp-art{position:absolute;left:0;top:0;width:1200px;height:462px;background:linear-gradient(90deg,#5b3b2d 0%,#9a7a9c 14%,#6fb0c4 22%,#c8c8c8 32%,#dedede 60%,#a9a9a9 85%,#7d7d7d 100%)}
.exp-box{position:absolute;left:463px;top:155px;width:492px;height:333px;background:var(--paper);border-bottom:1px solid var(--line);padding:0 54px}

/* schedule */
.schedule{top:2270px;height:440px}
.booker{position:absolute;left:586px;top:50px}
.booker .title{font-size:12px;font-weight:500;color:var(--ink)}
.month{position:absolute;left:0;top:34px;width:232px;font-size:11px;color:var(--text)}
.nav-arrows{position:absolute;left:196px;top:28px}
.cal{position:absolute;left:0;top:70px;display:grid;grid-template-columns:repeat(7,33px);grid-auto-rows:30px;font-size:9.5px;color:var(--text);text-align:center}
.cal span{display:flex;align-items:center;justify-content:center}
.cal .dow{font-size:9px;color:var(--ink)}
.cal .open i,.cal .pick i{font-style:normal;width:20px;height:20px;border-radius:50%;display:flex;align-items:center;justify-content:center}
.cal .open i{background:var(--chip);color:var(--ink)}
.cal .pick i{background:var(--ink);color:#fff}
.tz{position:absolute;left:0;top:308px;font-size:10.5px;color:var(--text);display:flex;align-items:center;gap:6px;white-space:nowrap}
.slots{position:absolute;left:252px;top:34px;width:118px}
.slots .date{font-size:10.5px;color:var(--ink);white-space:nowrap}
.slot{height:24px;border:1px solid #9a9a9a;font-size:10.5px;display:flex;align-items:center;justify-content:center;margin-top:7px;color:var(--ink)}
.slots .date + .slot{margin-top:18px}
.slot.on{background:var(--ink);color:#fff;border-color:var(--ink)}

/* footer */
.site-footer{top:2710px;height:290px;background:var(--night);color:#bdbdbd}
.site-footer .brand{border-color:#fff}
.site-footer .brand-name{color:#fff}
.site-footer .brand-sub{color:#aaa}
.socials{position:absolute;left:100px;top:148px;display:flex;gap:10px}
.socials span{width:22px;height:22px;border-radius:50%;border:1px solid #9a9a9a;display:block}
.copyright{position:absolute;left:100px;top:240px;font-size:11px;color:#a8a8a8}
.foot-nav{position:absolute;left:477px;top:58px;list-style:none;font-family:"Roboto Slab",Georgia,serif;font-size:11.5px;color:#a8a8a8;white-space:nowrap}
.foot-nav li{height:36.5px}
.foot-contact{position:absolute;left:858px;top:62px}
.foot-contact h4{font-family:"Roboto Slab",Georgia,serif;font-weight:400;font-size:16px;color:#fff}
.foot-contact .row{display:flex;align-items:center;gap:10px;font-family:"Roboto Slab",Georgia,serif;font-size:11.5px;color:#bdbdbd;margin-top:16px;white-space:nowrap}
.foot-contact .dot{width:20px;height:20px;border-radius:50%;background:#3a3a3a;display:flex;align-items:center;justify-content:center}
</style>
</head>
<body>

<section class="hero">
  <div class="hero-art" role="img" aria-label="Dark paper-cut profiles of many human heads layered together"></div>
  <div class="brand" style="left:100px;top:32px">
    <div class="brand-name">Dorian Pellquist</div>
    <div class="brand-sub">Doctor of Psychology</div>
  </div>
  <div class="hero-call">
    <svg width="12" height="12" viewBox="0 0 24 24"><path fill="#f4f4f4" d="M6.6 10.8a15 15 0 0 0 6.6 6.6l2.2-2.2c.3-.3.7-.4 1-.2 1.1.4 2.3.6 3.6.6.6 0 1 .4 1 1V20c0 .6-.4 1-1 1A17 17 0 0 1 3 4c0-.6.4-1 1-1h3.5c.6 0 1 .4 1 1 0 1.3.2 2.5.6 3.6.1.3 0 .7-.2 1z"/></svg>
    <span>Call for a consultation:</span><b>(415) 555-0188</b>
  </div>
  <svg class="menu" width="36" height="22" viewBox="0 0 36 22"><g stroke="#fff" stroke-width="2"><line x1="2" y1="2" x2="34" y2="2"/><line x1="2" y1="11" x2="34" y2="11"/><line x1="12" y1="20" x2="34" y2="20"/></g></svg>
  <h1 class="hero-title">Discover Healing and Growth<br>through Depth Psychotherapy<br>&amp; Consultation</h1>
  <p class="hero-lead">Embrace Your Inner Journey with a California Licensed<br>Psychologist in San Francisco</p>
  <a class="btn">Book an Appointment</a>
</section>

<section class="about">
  <div class="portrait" role="img" aria-label="Portrait photograph of the psychologist"></div>
  <div class="rule" style="left:560px;top:161px;width:84px"></div>
  <div class="eyebrow abs" style="left:656px;top:152px">About</div>
  <h2 class="heading abs" style="left:616px;top:183px">Empowering Transformation<br>through Depth Psychotherapy</h2>
  <p class="copy abs" style="left:616px;top:266px;width:366px">Unlock the potential of your mind and explore the depths of your psyche with our expert depth psychotherapy services. As a California Licensed Psychologist, I offer personalized and compassionate therapy for individuals and couples seeking healing and growth. Drawing on the insights of depth psychology, we delve into your unconscious, dreams, and archetypes to bring profound insights and facilitate positive changes in your life.</p>
  <div class="call-block">
    <div class="lbl"><svg width="11" height="11" viewBox="0 0 24 24"><path fill="#111" d="M6.6 10.8a15 15 0 0 0 6.6 6.6l2.2-2.2c.3-.3.7-.4 1-.2 1.1.4 2.3.6 3.6.6.6 0 1 .4 1 1V20c0 .6-.4 1-1 1A17 17 0 0 1 3 4c0-.6.4-1 1-1h3.5c.6 0 1 .4 1 1 0 1.3.2 2.5.6 3.6.1.3 0 .7-.2 1z"/></svg>Call for a consultation:</div>
    <div class="num">(415) 555-0188</div>
  </div>
</section>

<section class="services">
  <div class="rule" style="left:0;top:98px;width:250px"></div>
  <div class="eyebrow abs" style="left:264px;top:89px">Services</div>
  <h2 class="heading abs" style="left:236px;top:122px">Professional Clinical Consultation<br>and Training</h2>
  <p class="copy abs" style="left:236px;top:208px;width:420px">Unlock the potential of your mind and explore the depths of your<br>psyche with our expert depth psychotherapy services.</p>
  <div class="svc-art" role="img" aria-label="Sculpted head made of puzzle pieces with a red section"></div>
  <div class="badge">MENTAL<br>HEALTH</div>

  <div class="card" style="left:236px">
    <svg width="48" height="48" viewBox="0 0 48 48" fill="none" stroke="#333" stroke-width="1.5"><path d="M23 8c-4-3-10-1-10 4-5 0-7 6-4 9-3 3-2 9 3 10 0 5 6 8 11 5z"/><path d="M25 8c4-3 10-1 10 4 5 0 7 6 4 9 3 3 2 9-3 10 0 5-6 8-11 5z"/><path d="M16 18h5M16 26h6M27 18h5M26 26h6M24 8v30"/></svg>
    <h3>MINDFUL INSIGHTS</h3>
    <p>Harness the power of mindfulness for profound self-discovery and personal growth.</p>
    <svg class="go" width="22" height="10" viewBox="0 0 22 10"><path d="M0 5h20M16 1l4 4-4 4" stroke="#333" fill="none"/></svg>
  </div>
  <div class="card" style="left:487px">
    <svg width="50" height="44" viewBox="0 0 50 44" fill="none" stroke="#333" stroke-width="1.5"><path d="M25 40S4 27 4 14C4 7 9 3 15 3c5 0 8 3 10 6 2-3 5-6 10-6 6 0 11 4 11 11 0 13-21 26-21 26z"/><path d="M17 14h6v-3a3 3 0 0 1 6 0v3h4v6h-3a3 3 0 0 0 0 6h3v5"/></svg>
    <h3>RELATIONSHIP RENEW</h3>
    <p>Strengthen your connections and cultivate healthy relationships with expert guidance.</p>
    <svg class="go" width="22" height="10" viewBox="0 0 22 10"><path d="M0 5h20M16 1l4 4-4 4" stroke="#333" fill="none"/></svg>
  </div>
  <div class="card" style="left:738px">
    <svg width="50" height="44" viewBox="0 0 50 44" fill="none" stroke="#333" stroke-width="1.5"><circle cx="12" cy="8" r="4"/><path d="M8 14l-4 12h6l2 14M12 14l8 8 6-4M4 40h14"/><path d="M24 30h8v-6h8v-6h8M24 36h24"/><path d="M30 6l6 6M36 6v6h-6"/></svg>
    <h3>RESILIENCE BOOST</h3>
    <p>Develop inner strength and resilience to overcome life's challenges with resilience-focused support.</p>
    <svg class="go" width="22" height="10" viewBox="0 0 22 10"><path d="M0 5h20M16 1l4 4-4 4" stroke="#333" fill="none"/></svg>
  </div>
</section>

<section class="experience">
  <div class="exp-art" role="img" aria-label="Hands forming a heart around a colourful paper head on crumpled paper"></div>
  <div class="exp-box">
    <div class="rule" style="left:0;top:48px;width:64px"></div>
    <div class="eyebrow abs" style="left:76px;top:39px">Experience</div>
    <h2 class="heading abs" style="left:54px;top:70px">Education for Mental and Medical<br>Health Professionals</h2>
    <p class="copy abs" style="left:54px;top:155px;width:390px">In the ever-evolving landscape of mental and medical health, ongoing education is essential. Through our educational programs, stay updated with the latest advancements and best practices in the field of depth psychotherapy. From workshops to seminars, we offer comprehensive training opportunities to expand your knowledge and excel in your career.</p>
  </div>
</section>

<section class="schedule">
  <div class="rule" style="left:0;top:52px;width:256px"></div>
  <div class="eyebrow abs" style="left:269px;top:43px">Schedule a Call</div>
  <h2 class="heading abs" style="left:236px;top:75px">Telehealth Convenience</h2>
  <p class="copy abs" style="left:236px;top:128px;width:284px">In today's fast-paced world, accessing mental health services should be easy and flexible. That's why all our appointments are currently available via telehealth. Embrace the convenience of virtual sessions, where you can engage in therapy or consultations from the comfort of your own space, while still receiving the same high-quality care.</p>

  <div class="booker">
    <div class="title">Select a Date &amp; Time</div>
    <div class="month">July 2023</div>
    <svg class="nav-arrows" width="40" height="14" viewBox="0 0 40 14"><path d="M8 2L3 7l5 5M30 2l5 5-5 5" stroke="#111" fill="none" stroke-width="1.3"/></svg>
    <div class="cal">
      <span class="dow">SUN</span><span class="dow">MON</span><span class="dow">TUE</span><span class="dow">WED</span><span class="dow">THU</span><span class="dow">FRI</span><span class="dow">SAT</span>
      <span></span><span></span><span></span><span></span><span></span><span></span><span>1</span>
      <span>2</span><span>3</span><span>4</span><span>5</span><span>6</span><span>7</span><span>8</span>
      <span>9</span><span>10</span><span>11</span><span>12</span><span>13</span><span>14</span><span>15</span>
      <span>16</span><span>17</span><span>18</span><span>19</span><span>20</span><span>21</span><span class="open"><i>22</i></span>
      <span class="pick"><i>23</i></span><span class="open"><i>24</i></span><span class="open"><i>25</i></span><span class="open"><i>26</i></span><span class="open"><i>27</i></span><span class="open"><i>28</i></span><span class="open"><i>29</i></span>
      <span class="open"><i>30</i></span><span class="open"><i>31</i></span>
    </div>
    <div class="tz"><svg width="12" height="12" viewBox="0 0 24 24" fill="none" stroke="#333" stroke-width="2"><circle cx="12" cy="12" r="10"/><path d="M2 12h20M12 2c3 3 3 17 0 20M12 2c-3 3-3 17 0 20"/></svg>Eastern time - Us California (03: 32 pm) ▾</div>
    <div class="slots">
      <div class="date">Monday, July 23</div>
      <div class="slot">10:30 am</div>
      <div class="slot on">11:00 am</div>
      <div class="slot">11:30 am</div>
    </div>
  </div>
</section>

<footer class="site-footer">
  <div class="brand" style="left:100px;top:70px">
    <div class="brand-name">Dorian Pellquist</div>
    <div class="brand-sub">Doctor of Psychology</div>
  </div>
  <div class="socials"><span></span><span></span><span></span><span></span></div>
  <div class="copyright">© Dorian Pellquist 2023</div>
  <ul class="foot-nav">
    <li>Home</li>
    <li>Depth Psychotherapy</li>
    <li>Clinical Consultation &amp; Professional Development</li>
    <li>Curriculum Vitae &amp; Publications</li>
    <li>Practice Policies and Forms</li>
  </ul>
  <div class="foot-contact">
    <h4>Contact</h4>
    <div class="row"><span class="dot"><svg width="10" height="10" viewBox="0 0 24 24"><path fill="#ccc" d="M6.6 10.8a15 15 0 0 0 6.6 6.6l2.2-2.2c.3-.3.7-.4 1-.2 1.1.4 2.3.6 3.6.6.6 0 1 .4 1 1V20c0 .6-.4 1-1 1A17 17 0 0 1 3 4c0-.6.4-1 1-1h3.5c.6 0 1 .4 1 1 0 1.3.2 2.5.6 3.6.1.3 0 .7-.2 1z"/></svg></span>(415) 555-0188</div>
    <div class="row"><span class="dot"><svg width="10" height="10" viewBox="0 0 24 24"><rect x="2" y="5" width="20" height="14" fill="none" stroke="#ccc" stroke-width="2"/><path d="M2 5l10 8 10-8" fill="none" stroke="#ccc" stroke-width="2"/></svg></span>dpellquist@mailhaven.com</div>
  </div>
</footer>

</body>
</html>
```